Brightmoor Advisory

Looking for modern business cards.
Clean contemporary design.
Similar to this.
https://www.quorvexsearch.example/imgview?src=https%3A%2F%2Fimg.pellumcards.example%2Fprofessional_elegant_modern_black_plain_metal_business_card-a7c21e90b4d3f5e6a8b9c0d1e2f3a4b5_540.jpg&ref=https%3A%2F%2Fwww.pellumcards.example%2Fprofessional_elegant_modern_black_plain_metal_business_card-518273640192837465&id=7kQ2mZ9x-PL4TW&w=540&h=540&q=modern%20business%20cards

But I'd like the blue to look metallic.

```html
<!DOCTYPE html>
<html lang="en">
<head>
<meta charset="utf-8">
<title>Brightmoor Advisory – Business Cards</title>
<link rel="stylesheet" href="https://fonts.googleapis.com/css2?family=Arimo:wght@400;700&family=Open+Sans:wght@600&display=swap">
<style>
  :root {
    --backdrop: #dde1e8;
    --metal-deep: #3f5f8a;
    --metal-mid: #5a7ba6;
    --metal-light: #7f9cc2;
    --streak-light: rgba(255, 255, 255, 0.10);
    --streak-dark: rgba(20, 40, 70, 0.12);
    --logo-ink: #e4e9ef;
    --name-ink: #262b33;
    --contact-ink: #1f242b;
  }
  html, body {
    margin: 0;
    padding: 0;
    width: 1200px;
    height: 900px;
    overflow: hidden;
    background: var(--backdrop);
  }
  .canvas {
    position: relative;
    width: 1200px;
    height: 900px;
    background: linear-gradient(160deg, #eceff4 0%, var(--backdrop) 55%, #c9ced7 100%);
  }
  .card {
    position: absolute;
    width: 500px;
    height: 290px;
    border-radius: 3px;
    overflow: hidden;
    box-shadow: 0 14px 30px rgba(40, 50, 70, 0.25);
    background:
      repeating-linear-gradient(0deg, var(--streak-light) 0 1px, transparent 1px 3px, var(--streak-dark) 3px 4px, transparent 4px 7px),
      linear-gradient(115deg, var(--metal-deep) 0%, var(--metal-mid) 35%, var(--metal-light) 50%, var(--metal-mid) 65%, var(--metal-deep) 100%);
  }
  .card--front { left: 620px; top: 150px; }
  .card--back {
    left: 100px; top: 460px;
    background:
      repeating-linear-gradient(0deg, var(--streak-light) 0 1px, transparent 1px 3px, var(--streak-dark) 3px 4px, transparent 4px 7px),
      linear-gradient(115deg, var(--metal-mid) 0%, var(--metal-light) 40%, #93aed0 52%, var(--metal-light) 65%, var(--metal-mid) 100%);
  }
  .brand {
    position: absolute;
    right: 44px;
    top: 118px;
    display: flex;
    align-items: center;
    gap: 12px;
  }
  .brand__mark {
    width: 22px;
    height: 22px;
    border-radius: 50%;
    background: var(--logo-ink);
  }
  .brand__name {
    font-family: "Open Sans", sans-serif;
    font-weight: 600;
    font-size: 34px;
    line-height: 40px;
    color: var(--logo-ink);
    letter-spacing: 0.2px;
    white-space: nowrap;
  }
  .person {
    position: absolute;
    left: 70px;
    top: 70px;
    margin: 0;
    font-family: "Arimo", sans-serif;
    font-weight: 700;
    font-size: 30px;
    line-height: 36px;
    color: var(--name-ink);
  }
  .contact {
    position: absolute;
    left: 250px;
    top: 140px;
    margin: 0;
    padding: 2px 0 2px 10px;
    border-left: 1.5px solid var(--contact-ink);
    list-style: none;
    font-family: "Arimo", sans-serif;
    font-size: 14px;
    line-height: 17px;
    color: var(--contact-ink);
    white-space: nowrap;
  }
</style>
</head>
<body>
  <main class="canvas">
    <section class="card card--front" aria-label="Card front">
      <div class="brand">
        <span class="brand__name">Brightmoor Advisory</span>
        <span class="brand__mark" aria-hidden="true"></span>
      </div>
    </section>

    <section class="card card--back" aria-label="Card back">
      <h1 class="person">JOHN DOE</h1>
      <ul class="contact">
        <li>+41 76 555 01 42</li>
        <li>john.doe.example</li>
        <li>profiles.example/john.doe</li>
      </ul>
    </section>
  </main>
</body>
</html>
```